MCP phase 1 web design

Meridale Capital Partners Ltd (MCP) is a challenger business to the traditional leasing market. We look for solutions to complex problems involving the funding of capital equipment within an office environment and then build documentation around the solution. We recently created a brief for a logo and successfully completed that assignment. We now need to create our first web site which is simply intended to be informative. To help interested designers we have attached a detailed brief that is broken into three sections. The first explains how we see the site developing over time from something quite straightforward initially to a full transaction capability. Whoever wins this competition will be expected to work with us into the future to help develop the site. Section 2 gives you a view about our likes and dislikes by reviewing some existing sites. Section 3 gives you the structure and content of the site based upon our likes and dislikes. We are by no means committed to the structure and if you believe it can be presented in a better way then please use your design. The text is fixed as content. The images to appear can be anything from photographs to line drawings again entirely at the designers whim. Currently we have a home page plus 5 subsidiary pages. A few things to help you:
1. The logo is fixed and should be amongst the downloads.
2. The colours we have are corporate and should be used.
3. The typeface we use within the business is "Verdana"
Good luck.

Industry/Entity Type

Business

```html
<!DOCTYPE html>
<html lang="en">
<head>
<meta charset="utf-8">
<title>Why Alternative? – Meridale Capital Partners Ltd</title>
<link href="https://fonts.googleapis.com/css2?family=Noto+Sans:wght@400&display=swap" rel="stylesheet">
<style>
  :root {
    --brand-blue: #1a6fb5;
    --nav-grey: #555555;
    --text-black: #111111;
    --page-grey: #dedede;
    --page-light: #f2f2f2;
    --panel-white: #ffffff;
  }
  * { margin: 0; padding: 0; box-sizing: border-box; }
  html, body {
    width: 1200px; height: 1000px; overflow: hidden;
    background: var(--panel-white);
    font-family: Verdana, "Noto Sans", sans-serif;
  }
  .page {
    position: relative; width: 1200px; height: 898px;
    background: radial-gradient(ellipse 620px 480px at 600px 380px, var(--page-light), var(--page-grey));
  }
  .site-header {
    position: absolute; top: 0; left: 0; width: 1200px; height: 68px;
    background: var(--panel-white);
    border-top: 5px solid var(--brand-blue);
    box-shadow: 0 2px 3px rgba(0,0,0,0.45);
    z-index: 2;
  }
  .brand {
    position: absolute; left: 112px; top: 15px;
    display: flex; align-items: center; gap: 10px;
  }
  .brand-mark { width: 26px; height: 26px; background: var(--brand-blue); }
  .brand-name { font-size: 19px; color: var(--brand-blue); letter-spacing: 0.5px; }
  .main-nav a {
    position: absolute; top: 22px; transform: translateX(-50%);
    font-size: 17px; color: var(--nav-grey); text-decoration: none; white-space: nowrap;
  }
  .main-nav a.is-active { color: var(--brand-blue); }
  .nav-pointer { position: absolute; left: 680px; top: 50px; }
  .content-panel {
    position: absolute; left: 100px; top: 82px; width: 1000px; height: 574px;
    background: var(--panel-white); border-radius: 8px;
    padding: 20px 10px;
  }
  .content-panel h1 {
    font-weight: 400; font-size: 32px; color: var(--brand-blue);
    margin-bottom: 18px; letter-spacing: 0.3px;
  }
  .content-panel p {
    width: 845px; margin-left: 2px;
    font-size: 16px; line-height: 23px; color: var(--text-black);
  }
  .content-panel p + p { margin-top: 23px; }
</style>
</head>
<body>
<div class="page">
  <header class="site-header">
    <div class="brand">
      <span class="brand-mark"></span>
      <span class="brand-name">Meridale Capital Partners Ltd</span>
    </div>
    <nav class="main-nav">
      <a href="#" style="left:524px">HOME</a>
      <a href="#" class="is-active" style="left:688px">WHY ALTERNATIVE?</a>
      <a href="#" style="left:874px">SOLUTIONS</a>
      <a href="#" style="left:1046px">CONTACT</a>
    </nav>
    <svg class="nav-pointer" width="16" height="13" viewBox="0 0 16 13"><polygon points="8,0 16,13 0,13" fill="#5a5a5a"/></svg>
  </header>

  <main class="content-panel">
    <h1>Why Alternative?</h1>
    <p>In the ever changing world of print and technology projects, innovation and differentiation are key for successful VARs.&nbsp; MCP offers a new, fresh, ALTERNATIVE approach to the changing demands of the customer, designing specific contract and funding solutions to meet individual needs.<br>No longer is it possible to simply "offer a one fits all solution". We are not a production line. We spend our time understanding the issues and researching the results. We work closely with our VAR's and will bespoke solutions for them given their own peculiar requirements - if there is a solution we will find it.</p>
    <p>We boast our own suit of funding approved contracts, which enables us to work with VARs and their customers to make our solutions totally tailored to the needs of each projects.</p>
    <p>Please check our Managed Services, Public Sector and Education solutions, to find out more.</p>
  </main>
</div>
</body>
</html>
```